business card for trucking industry consulting firm

Our company, Velkor Services Inc. provides numerous services to the trucking industry as listed on our website: velkor.ca
The logo i want on the card is the black and red VELKOR
update: i would like the services we provide listed on the card (see velkor.ca)

```html
<!DOCTYPE html>
<html lang="en">
<head>
<meta charset="utf-8">
<title>Velkor Services Inc. – Business Card</title>
<link href="https://fonts.googleapis.com/css2?family=Oswald:wght@400;500;600&family=Roboto:ital,wght@0,400;0,500;1,400&display=swap" rel="stylesheet">
<style>
  :root {
    --red: #d0222b;
    --ink: #1b1718;
    --white: #ffffff;
    --stage: #e9e6e2;
    --text-dark: #151213;
  }
  * { margin: 0; padding: 0; box-sizing: border-box; }
  html, body { width: 900px; height: 1200px; overflow: hidden; }
  body { background: var(--stage); position: relative; font-family: "Roboto", sans-serif; }

  .card {
    position: absolute; left: 86px; width: 736px;
    border-radius: 22px; overflow: hidden;
    box-shadow: 0 6px 16px rgba(0,0,0,.25);
  }

  /* Front */
  .card-front { top: 137px; height: 428px; background: var(--white); }
  .tagline-band { position: absolute; top: 29px; left: 0; width: 100%; height: 23px; background: var(--red); }
  .tagline {
    position: absolute; top: 29px; left: 372px; height: 23px; padding: 0 0 0 8px;
    background: var(--white); font-style: italic; font-size: 14px; line-height: 23px; color: var(--text-dark);
  }
  .tagline .year { background: var(--red); color: var(--white); padding: 0 4px; margin-left: 2px; display: inline-block; }

  .brand { position: absolute; left: 52px; top: 104px; width: 274px; color: var(--text-dark);
    font-family: "Oswald", sans-serif; font-weight: 600; }
  .brand-name { font-size: 78px; line-height: 1; letter-spacing: 1px; }
  .brand-sub { font-size: 26px; letter-spacing: 5px; margin-top: 8px; padding-left: 2px; }

  .person { position: absolute; left: 379px; top: 100px; font-family: "Oswald", sans-serif; }
  .person-name { font-size: 26px; font-weight: 500; color: var(--text-dark); line-height: 1.1; }
  .person-name .first { color: var(--red); }
  .person-title { font-size: 21px; font-weight: 500; color: var(--text-dark); margin-top: 4px; }
  .contacts { list-style: none; margin-top: 24px; }
  .contacts li { display: flex; align-items: center; height: 30px; font-size: 20px; color: var(--text-dark); }
  .contacts svg { width: 20px; height: 20px; margin: 0 14px 0 0; fill: var(--red); }

  .address-band { position: absolute; top: 302px; left: 0; width: 100%; height: 75px; background: var(--ink);
    display: flex; align-items: center; justify-content: space-between; padding: 0 38px 0 42px;
    font-family: "Oswald", sans-serif; font-size: 20px; color: var(--white); }
  .address-band span { display: flex; align-items: center; }
  .address-band svg { width: 22px; height: 22px; fill: var(--red); margin-right: 6px; }
  .address-band .web svg { fill: none; stroke: var(--red); stroke-width: 2; margin-right: 10px; }
  .bottom-band { position: absolute; top: 377px; left: 0; width: 100%; height: 29px; background: var(--red); }

  /* Back */
  .card-back { top: 633px; height: 430px; background: var(--ink); }
  .services-label { position: absolute; left: 0; top: 0; width: 92px; height: 100%; background: var(--red); }
  .services-label .pointer { position: absolute; left: 92px; top: 193px; }
  .services-label h2 {
    position: absolute; left: 46px; top: 215px; transform: translate(-50%, -50%) rotate(-90deg);
    font-family: "Oswald", sans-serif; font-weight: 500; font-size: 40px; letter-spacing: 17px;
    color: var(--white); white-space: nowrap;
  }
  .edge-strip { position: absolute; right: 0; top: 0; width: 22px; height: 100%; background: var(--red); }
  .service-list { list-style: none; position: absolute; left: 129px; top: 40px;
    display: grid; grid-template-columns: 217px 360px; grid-auto-rows: 98px; }
  .service-list li { border-left: 5px solid var(--red); padding-left: 11px; height: 58px;
    font-size: 21px; line-height: 27px; color: var(--white); }
</style>
</head>
<body>

<section class="card card-front" aria-label="Business card front">
  <div class="tagline-band"></div>
  <p class="tagline">Transportation Compliance Specialists since <span class="year">1990</span></p>

  <div class="brand">
    <div class="brand-name">VELKOR</div>
    <div class="brand-sub">SERVICES INC.</div>
  </div>

  <div class="person">
    <div class="person-name"><span class="first">JOHNTAHAN</span> DOE</div>
    <div class="person-title">CEO</div>
    <ul class="contacts">
      <li><svg viewBox="0 0 24 24"><path d="M7 2h10a2 2 0 0 1 2 2v16a2 2 0 0 1-2 2H7a2 2 0 0 1-2-2V4a2 2 0 0 1 2-2zm0 2v16h10V4z"/></svg>123-456-7890</li>
      <li><svg viewBox="0 0 24 24"><path d="M6.6 10.8a15 15 0 0 0 6.6 6.6l2.2-2.2a1 1 0 0 1 1-.25 11.4 11.4 0 0 0 3.6.57 1 1 0 0 1 1 1V20a1 1 0 0 1-1 1A17 17 0 0 1 3 4a1 1 0 0 1 1-1h3.5a1 1 0 0 1 1 1c0 1.25.2 2.45.57 3.57a1 1 0 0 1-.25 1z"/></svg>780-555-0142</li>
      <li><svg viewBox="0 0 24 24"><path d="M2 5h20v2l-10 6L2 7zm0 4l10 6 10-6v10H2z"/></svg>EMAIL@VELKOR.CA</li>
    </ul>
  </div>

  <div class="address-band">
    <span><svg viewBox="0 0 24 24"><path d="M12 2a7 7 0 0 0-7 7c0 5 7 13 7 13s7-8 7-13a7 7 0 0 0-7-7zm0 9.5A2.5 2.5 0 1 1 12 6.5a2.5 2.5 0 0 1 0 5z"/></svg>#305, 8420-52 Ave, Edmonton, Alberta, T6E 2K4 Canada</span>
    <span class="web"><svg viewBox="0 0 24 24"><circle cx="12" cy="12" r="10"/><path d="M2 12h20M12 2c3 3 3 17 0 20M12 2c-3 3-3 17 0 20M4 7h16M4 17h16"/></svg>VELKOR.CA</span>
  </div>
  <div class="bottom-band"></div>
</section>

<section class="card card-back" aria-label="Business card back">
  <div class="services-label">
    <svg class="pointer" width="22" height="44" viewBox="0 0 22 44"><path d="M0 0L22 22L0 44Z" fill="#d0222b"/></svg>
    <h2>SERVICES</h2>
  </div>
  <ul class="service-list">
    <li>Prorate<br>Licensing</li>
    <li>IFTA Fuel<br>Tax Reporting</li>
    <li>Safety Fitness<br>Certificates (SFC)</li>
    <li>Travel to<br>USA</li>
    <li>Log Book<br>Auditing</li>
    <li>Written Safety &amp;<br>Maintenance Programs</li>
    <li>Compliance and<br>Audit Assistance</li>
    <li>Design and Printing of Log Books<br>and Trip Inspection books</li>
  </ul>
  <div class="edge-strip"></div>
</section>

</body>
</html>
```